Premium Gold Vodka Label Design

English ------------------- We need a label for a Vodka Bottle. Its a sparkling premium vodka with gold inside. The design should look premium. We tried it on our selves but it looks horrible. Therefore we need your help. The current name is lumora K, but we are open for any better suggestion. We attached the selfmade design. The label will be printed on the bottle. We have other design jobs for you (logo, other sorts)! English ------------------------ We need a label for a vodka bottle. This is a premium vodka which is offset with gold. The design should look like this. We have tried so far and failed. That is why we need your support. The name is so far lumora K. If you have better suggestions we would be pleased about other suggestions / ideas. In the appendix the failed design is stored. The label is to be applied by screen printing. In the case of good work follow-up projects are guaranteed (logo, other varieties, etc)!
Updates

Project Deadline Extended
Reason: We need more time for the decision.

Target Market(s)

USA

Colors

Designer to choose colors to be used in the design.

Requirements
Must have
• English ------------------------ The needed text is on our selfmade label that is attached. English ------------------------ The required texts are stored in the attached design.
Nice to have
• English ------------------------ Transparent places are allowed because we want to print the label on the bottom. English ------------------------ As the label is applied by screen printing, transparent areas are also possible.

```html
<!DOCTYPE html>
<html lang="en">
<head>
<meta charset="utf-8">
<title>lumora K – Premium Gold Sparkling Vodka Label</title>
<link href="https://fonts.googleapis.com/css2?family=Didact+Gothic&family=Michroma&family=Great+Vibes&family=Comfortaa:wght@500&display=swap" rel="stylesheet">
<style>
  :root {
    --stage: #a89a5c;
    --ink: #0b0b08;
    --pattern-dark: #17160f;
    --pattern-mid: #3a3726;
    --panel-top: #4a4636;
    --panel-gold: #e6d47a;
    --panel-deep: #8d8150;
    --band: rgba(225, 220, 185, 0.75);
    --band-light: #eee6b4;
    --band-shade: #9c9880;
    --cream: #efe6b8;
  }
  * { box-sizing: border-box; margin: 0; padding: 0; }
  html, body { width: 1200px; height: 1000px; overflow: hidden; }
  body { background: var(--stage); position: relative; }

  .label {
    position: absolute; left: 440px; top: 285px;
    width: 320px; height: 430px;
    border: 2px solid var(--ink);
  }
  .label__pattern {
    position: absolute; inset: 0;
    background: radial-gradient(ellipse at center, var(--pattern-mid), var(--pattern-dark));
  }
  .label__panel {
    position: absolute; left: 13px; top: 12px; width: 292px; height: 402px;
    border-radius: 30px;
    border: 1px solid #222;
    background: linear-gradient(180deg, var(--panel-top) 0%, #6e6a55 18%, var(--panel-gold) 58%, #b9a95f 82%, var(--panel-deep) 100%);
  }
  .label__band {
    position: absolute; left: 0; top: 62px; width: 316px; height: 156px;
    background: var(--band);
  }
  .label__band-inner {
    position: absolute; left: 15px; top: 62px; width: 286px; height: 156px;
    border: 1px solid #77735f;
    background: linear-gradient(160deg, #a6a28a 0%, #b8b394 40%, var(--band-light) 80%, #f2eab8 100%);
  }
  .brand {
    position: absolute; left: 15px; width: 286px; text-align: center;
    font-family: "Didact Gothic", sans-serif; font-weight: 400; color: var(--ink);
  }
  .brand--word { top: 68px; font-size: 44px; line-height: 52px; letter-spacing: -0.5px; }
  .brand--letter { top: 112px; font-size: 104px; line-height: 104px; }

  .tagline {
    position: absolute; left: 0; width: 316px; top: 222px; text-align: center;
    font-family: "Michroma", sans-serif; font-size: 10.5px; letter-spacing: 0.6px; color: var(--ink);
  }
  .product {
    position: absolute; left: 0; width: 316px; top: 236px; text-align: center;
    font-family: "Great Vibes", cursive; font-size: 62px; line-height: 80px; color: var(--ink);
  }
  .process {
    position: absolute; left: 0; width: 316px; top: 316px; text-align: center;
    font-family: "Michroma", sans-serif; font-size: 14.5px; letter-spacing: 1px; color: var(--ink);
    display: flex; justify-content: center; align-items: center; gap: 2px;
  }
  .process__num {
    font-size: 34px; line-height: 34px; color: transparent;
    -webkit-text-stroke: 1.5px var(--ink);
  }
  .origin {
    position: absolute; left: 0; width: 316px; top: 362px; text-align: center;
    font-family: "Great Vibes", cursive; font-size: 16px; color: var(--cream);
  }
  .rule {
    position: absolute; left: 38px; width: 242px; top: 385px; height: 1px; background: rgba(239,230,184,0.6);
  }
  .specs {
    position: absolute; left: 38px; width: 242px; top: 390px;
    display: flex; justify-content: space-between;
    font-family: "Comfortaa", sans-serif; font-weight: 500; font-size: 12.5px; color: var(--cream);
  }
</style>
</head>
<body>
  <div class="label">
    <div class="label__pattern" role="img" aria-label="Dark ornamental line-art pattern border"></div>
    <div class="label__panel"></div>
    <div class="label__band"></div>
    <div class="label__band-inner"></div>
    <div class="brand brand--word">lumora</div>
    <div class="brand brand--letter">K</div>
    <p class="tagline">PREMIUM GOLD SPARKLING</p>
    <p class="product">Vodka</p>
    <p class="process"><span>DISTILLED</span><span class="process__num">8</span><span>FILTERED</span></p>
    <p class="origin">Made in Germany</p>
    <div class="rule"></div>
    <div class="specs"><span>40%Alc Vol</span><span>200ml</span><span>80Proof</span></div>
  </div>
</body>
</html>
```